Flash Banners for CourseLantern.com

We are running a media campaign to drive traffic to CourseLantern.com. Course Lantern allows people that are interested in pursuing an advanced degree to find colleges and universities that offer their program and level of study.

We would like to have Flash Interactive banners created that grab people’s attention and have a high click-thru rate for our CPM Media Campaign.

BANNER MESSAGING/CLICKABLE ELEMENTS:
Headline: Earn Your Degree Online!

Clickable Elements with Rollover Animation and/or Icons:
GROUPING 1
Nursing
Business
Education
Legal
Design
And more
GROUPING 2
Associates
Bachelor’s
Master’s
Doctorate
(Each group should have some kind of visual separation, no need to label
Group1 or Group 2)

Call To Action: Find Schools

Logo: CourseLantern

Industry/Entity Type

Business

Requirements
Must have
• We would like animated flash banners in the following sizes:
300x250
728x90
160x600

The spec requirements are:
24 FPS (Frames per second)
30 seconds max animation, looping back to beginning
120K Max File Size
Final .swf file & Original .FLA file with layers

```html
<!DOCTYPE html>
<html lang="en">
<head>
<meta charset="utf-8">
<title>CourseLantern Banners</title>
<link rel="stylesheet" href="https://fonts.googleapis.com/css2?family=PT+Sans:wght@400;700&family=PT+Sans+Narrow:wght@700&display=swap">
<style>
  :root {
    --stage: #5d6068;
    --label: #ffffff;
    --blue-top: #1c8fcf;
    --blue-bottom: #0b4a86;
    --blue-deep: #083d73;
    --orange-top: #f39324;
    --orange-bottom: #e2650f;
    --orange-deep: #c4520a;
    --btn-orange-top: #f07a30;
    --btn-orange-dark: #c14a0e;
    --btn-blue-top: #3fa2f2;
    --btn-blue-dark: #1466c0;
    --brand: #24485a;
    --brand-mark: #e8621a;
    --text: #ffffff;
    --hl-blue: rgba(6, 52, 110, 0.65);
    --hl-orange: rgba(190, 80, 8, 0.75);
  }
  * { box-sizing: border-box; margin: 0; padding: 0; }
  html, body { width: 1200px; height: 900px; overflow: hidden; }
  body {
    background: var(--stage);
    position: relative;
    font-family: "PT Sans", Arial, sans-serif;
  }
  .group-label {
    position: absolute;
    top: 176px;
    width: 450px;
    text-align: center;
    color: var(--label);
    font-family: "PT Sans Narrow", "Arial Narrow", sans-serif;
    font-weight: 700;
    font-size: 38px;
  }
  .banner {
    position: absolute;
    top: 264px;
    width: 450px;
    height: 375px;
    overflow: hidden;
    border: 2px solid #e9eef3;
  }
  .banner--subjects { left: 123px; background: linear-gradient(180deg, var(--blue-top), var(--blue-bottom)); }
  .banner--levels {
    left: 618px;
    background:
      radial-gradient(ellipse 60% 45% at 60% 55%, rgba(255,190,90,0.45), transparent 70%),
      linear-gradient(180deg, var(--orange-top), var(--orange-bottom));
  }
  .headline {
    position: absolute;
    top: 20px; left: 0; width: 100%;
    text-align: center;
    color: var(--text);
    font-family: "PT Sans Narrow", "Arial Narrow", sans-serif;
    font-weight: 700;
    font-size: 39px;
    letter-spacing: -0.3px;
    text-shadow: 0 2px 2px rgba(0,0,0,0.25);
  }
  .option {
    position: absolute;
    height: 42px;
    display: flex;
    align-items: center;
    color: var(--text);
    font-size: 25px;
  }
  .option__icon {
    width: 20px; height: 20px;
    border-radius: 4px;
    margin-right: 20px;
    flex: none;
  }
  .option--active { border-radius: 3px; }
  .banner--subjects .option--active { background: var(--hl-blue); }
  .banner--levels .option--active { background: var(--hl-orange); }
  .footer-wave { position: absolute; left: 0; bottom: 0; width: 450px; height: 120px; z-index: 1; }
  .cta {
    position: absolute;
    z-index: 2;
    top: 236px; left: 133px;
    width: 180px; height: 42px;
    border-radius: 5px;
    color: var(--text);
    font-weight: 700;
    font-size: 22px;
    display: flex; align-items: center; justify-content: center;
    box-shadow: 0 2px 3px rgba(0,0,0,0.3);
  }
  .cta--orange { background: linear-gradient(180deg, var(--btn-orange-top), var(--btn-orange-dark)); }
  .cta--blue { background: linear-gradient(180deg, var(--btn-blue-top), var(--btn-blue-dark)); }
  .brand {
    position: absolute;
    z-index: 2;
    left: 108px; top: 316px;
    display: flex; align-items: center;
    color: var(--brand);
    font-weight: 700;
    font-size: 38px;
    letter-spacing: -0.5px;
  }
  .brand__square {
    width: 24px; height: 24px;
    background: var(--brand-mark);
    margin-left: 14px;
  }
</style>
</head>
<body>
  <div class="group-label" style="left:123px">GROUP 1</div>
  <div class="group-label" style="left:618px">GROUP 2</div>

  <section class="banner banner--subjects">
    <h1 class="headline">EARN YOUR DEGREE ONLINE!</h1>
    <div class="option" style="left:44px;top:81px"><span class="option__icon" role="img" aria-label="Nurse icon" style="background:#dfe7ef"></span>Nursing</div>
    <div class="option option--active" style="left:31px;top:129px;width:181px;padding-left:13px"><span class="option__icon" role="img" aria-label="Business person icon" style="background:#c9d2dc"></span>Business</div>
    <div class="option" style="left:44px;top:174px"><span class="option__icon" role="img" aria-label="Book icon" style="background:#eef2f6"></span>Education</div>
    <div class="option" style="left:266px;top:81px"><span class="option__icon" role="img" aria-label="Gavel icon" style="background:#f2b632"></span>Legal</div>
    <div class="option" style="left:266px;top:128px"><span class="option__icon" role="img" aria-label="Paint palette icon" style="background:#f1d9b8"></span>Design</div>
    <div class="option" style="left:266px;top:174px"><span class="option__icon" role="img" aria-label="Person with plus icon" style="background:#d6e6c8"></span>And more</div>
    <div class="cta cta--orange">Find Schools</div>
    <svg class="footer-wave" viewBox="0 0 450 120" preserveAspectRatio="none">
      <defs><linearGradient id="footSubjects" x1="0" x2="1"><stop offset="0" stop-color="#d3dcea"/><stop offset="0.5" stop-color="#ffffff"/><stop offset="1" stop-color="#ffffff"/></linearGradient></defs>
      <path d="M0,42 C150,52 320,44 450,22 L450,120 L0,120Z" fill="var(--blue-deep)"/>
      <path d="M0,50 C150,60 320,52 450,33 L450,120 L0,120Z" fill="url(#footSubjects)"/>
    </svg>
    <div class="brand">courselantern<span class="brand__square"></span></div>
  </section>

  <section class="banner banner--levels">
    <h1 class="headline">EARN YOUR DEGREE ONLINE!</h1>
    <div class="option option--active" style="left:31px;top:81px;width:180px;padding-left:13px"><span class="option__icon" role="img" aria-label="Graduate icon" style="background:#9ccf7a"></span>Associates</div>
    <div class="option" style="left:44px;top:128px"><span class="option__icon" role="img" aria-label="Graduate icon" style="background:#f6e2c8"></span>Bachelor’s</div>
    <div class="option" style="left:264px;top:81px"><span class="option__icon" role="img" aria-label="Graduate icon" style="background:#8a5a34"></span>Master’s</div>
    <div class="option" style="left:264px;top:128px"><span class="option__icon" role="img" aria-label="Graduate icon" style="background:#6e4a2c"></span>Doctorate</div>
    <div class="cta cta--blue">Find Schools</div>
    <svg class="footer-wave" viewBox="0 0 450 120" preserveAspectRatio="none">
      <defs><linearGradient id="footLevels" x1="0" x2="1"><stop offset="0" stop-color="#f6dcc6"/><stop offset="0.5" stop-color="#ffffff"/><stop offset="1" stop-color="#ffffff"/></linearGradient></defs>
      <path d="M0,42 C150,52 320,44 450,22 L450,120 L0,120Z" fill="var(--orange-deep)"/>
      <path d="M0,50 C150,60 320,52 450,33 L450,120 L0,120Z" fill="url(#footLevels)"/>
    </svg>
    <div class="brand">courselantern<span class="brand__square"></span></div>
  </section>
</body>
</html>
```